Verpackungen für elektronische Entspannungsgeräte
You did a great job!!! Thank you very much and thank you for your patience as well. It was great working with you. Many Greetings from Germany :-))) Tessa
Zielgruppe
Wir stellen elektronische Entspannungsgeräte her. Für Jedermann, jeden Alters.
Aufgabenstellung
Jetzt bäuchte ich für eine Umverpackung ein Design. Außen auf der Verpackung soll das Design drauf und innen auf der Deckelseite soll in schöner Schrift stehen:
'Herzlichen Glückwunsch zu einem entspannteren Leben :-)'
Das Design auf der Verpackung soll viel weiß enthalten. Es soll elegant, aber schlicht gehalten sein, in den gleichen Farben wie das Logo.
Die Umverpackung wird ca. 15 x 10 x 4 cm groß sein. Bitte eine Vektorgrafik, die ich entsprechend vergrößern kann.
CE sollte drauf.
Vorsel GmbH, www.vorsel-gmbh.example; Am Querweg 14, 65491 Ostrach
Ich freue mich auf Vorschläge :-)

```html
<!DOCTYPE html>
<html lang="de">
<head>
<meta charset="utf-8">
<title>Vorsel – Made to Relax Verpackung</title>
<link rel="stylesheet" href="https://fonts.googleapis.com/css2?family=Jost:wght@600;700&family=Lobster&display=swap">
<style>
  :root {
    --stage: #e4e5e1;
    --lid: #ffffff;
    --ink: #333333;
    --brand-navy: #0f3a5a;
    --brand-teal: #23b3c4;
    --pastel-pink: #f4cbe6;
    --pastel-mint: #a6ecdf;
  }
  * { margin: 0; padding: 0; box-sizing: border-box; }
  html, body {
    width: 1200px;
    height: 1200px;
    overflow: hidden;
    background: var(--stage);
  }
  .canvas {
    position: relative;
    width: 1200px;
    height: 1200px;
  }
  .lid-artwork {
    position: absolute;
    left: 105px;
    top: 271px;
    width: 990px;
    height: 658px;
    background: var(--lid);
    box-shadow: 0 3px 5px rgba(0,0,0,0.25);
    overflow: hidden;
  }
  .brand {
    position: absolute;
    left: 104px;
    top: 118px;
    display: flex;
    align-items: center;
    gap: 10px;
    z-index: 1;
  }
  .brand-dot {
    width: 18px;
    height: 18px;
    border-radius: 50%;
    background: var(--brand-teal);
  }
  .brand-name {
    font-family: "Jost", sans-serif;
    font-weight: 600;
    font-size: 36px;
    line-height: 1;
    color: var(--brand-navy);
  }
  .claim-top {
    position: absolute;
    left: 279px;
    top: 262px;
    font-family: "Jost", sans-serif;
    font-weight: 700;
    font-size: 34px;
    letter-spacing: 2px;
    color: var(--ink);
    line-height: 1;
    z-index: 1;
  }
  .claim-script {
    position: absolute;
    left: 305px;
    top: 300px;
    font-family: "Lobster", cursive;
    font-size: 74px;
    color: var(--ink);
    line-height: 1;
    z-index: 1;
  }
  .colour-band {
    position: absolute;
    left: 0;
    top: 0;
    width: 990px;
    height: 658px;
  }
</style>
</head>
<body>
<main class="canvas">
  <section class="lid-artwork">
    <svg class="colour-band" viewBox="0 0 990 658" role="img" aria-label="Dekorative Pastellfläche in Rosa und Mint">
      <defs>
        <linearGradient id="bandFill" x1="0" y1="0" x2="1" y2="0">
          <stop offset="0" stop-color="var(--pastel-pink)"/>
          <stop offset="1" stop-color="var(--pastel-mint)"/>
        </linearGradient>
      </defs>
      <path d="M0 373 L460 454 L990 293 L990 658 L0 658 Z" fill="url(#bandFill)"/>
    </svg>

    <div class="brand">
      <span class="brand-dot"></span>
      <span class="brand-name">Vorsel</span>
    </div>
    <p class="claim-top">MADE TO</p>
    <p class="claim-script">Relax</p>
  </section>
</main>
</body>
</html>
```